Graphics for Corvella telehealth weight loss plans

Corvella focuses on delivering medical weight-loss using prescription medicine and telehealth consults. Corvella needs graphics for its ecommerce site for three weight loss plans. The plans are posted here with current graphics and descriptions of what is included with each plan. Please do not feel constrained by current graphics or styling.

- https://store.corvellacare.com/products/radiant-horizon-plan
- https://store.corvellacare.com/products/brightpath-core-plan
- https://store.corvellacare.com/products/daily-harbor-plan

The graphics need to look good on mobile and desktop browsers.

```html
<!DOCTYPE html>
<html lang="en">
<head>
<meta charset="utf-8">
<title>Corvella Plan Graphics</title>
<link href="https://fonts.googleapis.com/css2?family=Nunito:ital,wght@0,700;0,800;0,900;1,600&family=Assistant:wght@400;600;700&display=swap" rel="stylesheet">
<style>
  :root {
    --ink: #121212;
    --muted: #5a5a5a;
    --body: #3d3d3d;
    --coral: #f58a7a;
    --coral-ring: #fbb3a7;
    --sun: #f6d43e;
    --maroon: #4a1422;
    --white: #ffffff;
  }
  * { box-sizing: border-box; margin: 0; padding: 0; }
  html, body { width: 1200px; height: 1121px; overflow: hidden; background: var(--white); }
  .canvas { position: relative; width: 1200px; height: 1121px; font-family: "Assistant", sans-serif; }

  .poster { position: absolute; top: 39px; width: 358px; height: 481px; display: block; }
  .poster--horizon { left: 40px; }
  .poster--brightpath { left: 421px; }
  .poster--harbor { left: 800px; }
  .poster text, .product-shot text { font-family: "Nunito", sans-serif; }
  .title { font-weight: 900; fill: var(--white); text-anchor: middle; }
  .sub { font-weight: 800; text-anchor: middle; }
  .note { font-weight: 600; font-style: italic; fill: var(--white); text-anchor: middle; opacity: .85; }
  .brand { font-weight: 800; fill: var(--white); text-anchor: middle; letter-spacing: .4px; }
  .badge { fill: var(--coral); stroke: var(--coral-ring); stroke-width: 3; }
  .badge-text { font-weight: 900; fill: var(--white); text-anchor: middle; }

  .store-header { position: absolute; top: 566px; left: 302px; width: 700px; height: 30px; display: flex; align-items: center; }
  .store-name { font-size: 12px; font-weight: 700; color: var(--ink); width: 60px; }
  .store-nav { display: flex; gap: 18px; font-size: 9.5px; color: var(--muted); letter-spacing: .3px; }
  .store-nav span { display: flex; align-items: center; gap: 4px; }
  .store-icons { position: absolute; left: 624px; top: 6px; display: flex; gap: 14px; }

  .product-shot { position: absolute; left: 302px; top: 629px; width: 312px; height: 409px; display: block; }
  .product-info { position: absolute; left: 652px; top: 628px; width: 340px; color: var(--body); }
  .product-title { font-size: 27px; font-weight: 400; color: var(--ink); line-height: 36px; letter-spacing: .3px; }
  .product-price { margin-top: 14px; font-size: 12px; color: var(--ink); letter-spacing: .5px; }
  .billing { margin-top: 20px; font-size: 12.5px; color: var(--muted); }
  .control { margin-top: 17px; font-size: 10.5px; color: var(--muted); }
  .buy { margin-top: 18px; width: 311px; height: 34px; background: var(--ink); color: var(--white); font-size: 9.5px; font-weight: 600; letter-spacing: .6px; display: flex; align-items: center; justify-content: center; }
  .desc { margin-top: 18px; font-size: 10.5px; line-height: 20px; color: var(--muted); }
  .includes { margin-top: 12px; font-size: 10.5px; color: var(--muted); }
  .include-list { margin-top: 12px; padding-left: 14px; font-size: 10.5px; line-height: 20.4px; color: var(--muted); }
  .include-list strong, .exclusion strong { color: var(--ink); font-weight: 700; }
  .exclusion { margin-top: 11px; font-size: 10.5px; color: var(--muted); }
</style>
</head>
<body>
<div class="canvas">

  <svg class="poster poster--horizon" viewBox="0 0 358 481" aria-label="Radiant Horizon Plan graphic">
    <defs>
      <linearGradient id="bgHorizon" x1="0" y1="0" x2="0" y2="1"><stop offset="0" stop-color="#7c7cba"/><stop offset=".55" stop-color="#8a6aa8"/><stop offset="1" stop-color="#5b3a78"/></linearGradient>
      <linearGradient id="artHorizon" x1="0" y1="0" x2="0" y2="1"><stop offset="0" stop-color="#4f8f6a" stop-opacity="0"/><stop offset=".3" stop-color="#4c9a72"/><stop offset=".6" stop-color="#3f2a63"/><stop offset=".85" stop-color="#e6c2bd"/><stop offset="1" stop-color="#e9c9c4"/></linearGradient>
    </defs>
    <rect width="358" height="481" fill="url(#bgHorizon)"/>
    <rect y="190" width="358" height="291" fill="url(#artHorizon)" role="img" aria-label="Illustration of tropical leaves and flowers growing from a resting woman's head"/>
    <text class="brand" x="179" y="34" font-size="12">Corvella</text>
    <text class="title" x="179" y="78" font-size="29">Radiant</text>
    <text class="title" x="179" y="108" font-size="29">Horizon</text>
    <text class="title" x="179" y="138" font-size="29">Plan</text>
    <text class="sub" x="179" y="159" font-size="15" fill="var(--sun)">Physician consultation</text>
    <text class="sub" x="179" y="176" font-size="15" fill="var(--sun)">phentermine program</text>
    <text class="note" x="179" y="190" font-size="7.5">Month To Month/Pay as you go</text>
    <circle class="badge" cx="185" cy="261" r="62"/>
    <text class="badge-text" font-size="17.5"><tspan x="185" y="245">Expert</tspan><tspan x="185" y="266">Nutrition</tspan><tspan x="185" y="287">Consult</tspan></text>
    <circle class="badge" cx="67" cy="336" r="63"/>
    <text class="badge-text" font-size="11.5"><tspan x="67" y="320">Custom Crafted</tspan><tspan x="67" y="334">Diet Plan</tspan><tspan x="67" y="348">To Achieve</tspan><tspan x="67" y="363">Your Goals</tspan></text>
    <circle class="badge" cx="307" cy="314" r="54"/>
    <text class="badge-text" font-size="11"><tspan x="307" y="293">Nutritionist</tspan><tspan x="307" y="307">Coaching</tspan><tspan x="307" y="321">To Improve</tspan><tspan x="307" y="335">Your Health</tspan><tspan x="307" y="348">And Vitality</tspan></text>
  </svg>

  <svg class="poster poster--brightpath" viewBox="0 0 358 481" aria-label="Brightpath Core Plan graphic">
    <defs>
      <linearGradient id="bgBright" x1="0" y1="0" x2="0" y2="1"><stop offset="0" stop-color="#66c2b6"/><stop offset=".55" stop-color="#3f8e97"/><stop offset="1" stop-color="#2c5f7a"/></linearGradient>
      <linearGradient id="artBright" x1="0" y1="0" x2="0" y2="1"><stop offset="0" stop-color="#2f6b5a" stop-opacity="0"/><stop offset=".3" stop-color="#2d6a6a"/><stop offset=".6" stop-color="#2a2a72"/><stop offset=".85" stop-color="#e6c2bd"/><stop offset="1" stop-color="#e9c9c4"/></linearGradient>
    </defs>
    <rect width="358" height="481" fill="url(#bgBright)"/>
    <rect y="190" width="358" height="291" fill="url(#artBright)" role="img" aria-label="Illustration of tropical leaves and flowers growing from a resting woman's head"/>
    <text class="brand" x="179" y="34" font-size="12">Corvella</text>
    <text class="title" x="179" y="81" font-size="29">Brightpath</text>
    <text class="title" x="179" y="111" font-size="29">Core Plan</text>
    <text class="sub" x="179" y="133" font-size="15" fill="var(--sun)">Physical Consultation</text>
    <text class="sub" x="179" y="151" font-size="15" fill="var(--sun)">Phentermine Program</text>
    <text class="note" x="173" y="167" font-size="7.5">MONTH TO MONTH/PAY AS YOU GO</text>
    <circle class="badge" cx="185" cy="261" r="62"/>
    <text class="badge-text" font-size="17.5"><tspan x="185" y="245">Expert</tspan><tspan x="185" y="266">Nutrition</tspan><tspan x="185" y="287">Consult</tspan></text>
    <circle class="badge" cx="67" cy="336" r="63"/>
    <text class="badge-text" font-size="11.5"><tspan x="67" y="320">Custom Crafted</tspan><tspan x="67" y="334">Diet Plan</tspan><tspan x="67" y="348">To Achieve</tspan><tspan x="67" y="363">Your Goals</tspan></text>
    <circle class="badge" cx="305" cy="314" r="56"/>
    <text class="badge-text" font-size="11"><tspan x="305" y="293">Free</tspan><tspan x="305" y="307">Introductory</tspan><tspan x="305" y="321">Nutritionist</tspan><tspan x="305" y="335">consult on your</tspan><tspan x="305" y="348">first month</tspan></text>
  </svg>

  <svg class="poster poster--harbor" viewBox="0 0 358 481" aria-label="Daily Harbor Plan graphic">
    <defs>
      <linearGradient id="bgHarbor" x1="0" y1="0" x2="0" y2="1"><stop offset="0" stop-color="#e4866c"/><stop offset=".5" stop-color="#eaa866"/><stop offset="1" stop-color="#e0a060"/></linearGradient>
      <linearGradient id="artHarbor" x1="0" y1="0" x2="0" y2="1"><stop offset="0" stop-color="#2f5e62" stop-opacity="0"/><stop offset=".3" stop-color="#3b7a5a"/><stop offset=".6" stop-color="#5a2222"/><stop offset=".85" stop-color="#e6c2bd"/><stop offset="1" stop-color="#e9c9c4"/></linearGradient>
    </defs>
    <rect width="358" height="481" fill="url(#bgHarbor)"/>
    <rect y="190" width="358" height="291" fill="url(#artHarbor)" role="img" aria-label="Illustration of tropical leaves and flowers growing from a resting woman's head"/>
    <text class="brand" x="179" y="34" font-size="12">Corvella</text>
    <text class="title" x="179" y="81" font-size="29">Daily</text>
    <text class="title" x="179" y="111" font-size="29">Harbor Plan</text>
    <text class="sub" x="179" y="133" font-size="15" fill="var(--maroon)">Physical Consultation</text>
    <text class="sub" x="179" y="151" font-size="15" fill="var(--maroon)">Phentermine Program</text>
    <text class="note" x="173" y="167" font-size="7.5">MONTH TO MONTH/PAY AS YOU GO</text>
    <circle class="badge" cx="185" cy="261" r="62"/>
    <text class="badge-text" font-size="17.5"><tspan x="185" y="245">Expert</tspan><tspan x="185" y="266">Nutrition</tspan><tspan x="185" y="287">Consult</tspan></text>
    <circle class="badge" cx="67" cy="336" r="63"/>
    <text class="badge-text" font-size="11.5"><tspan x="67" y="320">Custom Crafted</tspan><tspan x="67" y="334">Diet Plan</tspan><tspan x="67" y="348">To Achieve</tspan><tspan x="67" y="363">Your Goals</tspan></text>
    <circle class="badge" cx="307" cy="314" r="54"/>
    <text class="badge-text" font-size="11"><tspan x="307" y="293">Nutritionist</tspan><tspan x="307" y="307">Coaching</tspan><tspan x="307" y="321">To Improve</tspan><tspan x="307" y="335">Your Health</tspan><tspan x="307" y="348">And Vitality</tspan></text>
  </svg>

  <header class="store-header">
    <div class="store-name">Corvella</div>
    <nav class="store-nav">
      <span>Testimonials</span>
      <span>Help <svg width="8" height="6" viewBox="0 0 8 6"><path d="M1 1.5l3 3 3-3" fill="none" stroke="#555" stroke-width="1"/></svg></span>
      <span>About</span>
      <span>Contact</span>
    </nav>
    <div class="store-icons">
      <svg width="16" height="16" viewBox="0 0 16 16"><circle cx="6.5" cy="6.5" r="5" fill="none" stroke="#121212" stroke-width="1.2"/><path d="M10.3 10.3l4.5 4.5" stroke="#121212" stroke-width="1.2"/></svg>
      <svg width="16" height="16" viewBox="0 0 16 16"><circle cx="8" cy="5" r="3.2" fill="none" stroke="#121212" stroke-width="1.2"/><path d="M2 15c0-3.5 2.7-5.5 6-5.5s6 2 6 5.5z" fill="none" stroke="#121212" stroke-width="1.2"/></svg>
      <svg width="16" height="16" viewBox="0 0 16 16"><path d="M2 4h12v11H2z" fill="none" stroke="#121212" stroke-width="1.2"/><path d="M5.5 6V3.5a2.5 2.5 0 015 0V6" fill="none" stroke="#121212" stroke-width="1.2"/></svg>
    </div>
  </header>

  <svg class="product-shot" viewBox="23 0 312 409" preserveAspectRatio="xMidYMid slice" aria-label="Daily Harbor Plan product graphic">
    <rect width="358" height="481" fill="url(#bgHarbor)"/>
    <rect y="190" width="358" height="291" fill="url(#artHarbor)" role="img" aria-label="Illustration of tropical leaves and flowers growing from a resting woman's head"/>
    <text class="brand" x="179" y="34" font-size="12">Corvella</text>
    <text class="title" x="179" y="81" font-size="27">Daily</text>
    <text class="title" x="179" y="109" font-size="27">Harbor Plan</text>
    <text class="sub" x="179" y="130" font-size="13.5" fill="var(--maroon)">Physical Consultation</text>
    <text class="sub" x="179" y="146" font-size="13.5" fill="var(--maroon)">Phentermine Program</text>
    <text class="note" x="173" y="161" font-size="7">MONTH TO MONTH/PAY AS YOU GO</text>
    <circle class="badge" cx="183" cy="235" r="53"/>
    <text class="badge-text" font-size="15"><tspan x="183" y="221">Expert</tspan><tspan x="183" y="239">Nutrition</tspan><tspan x="183" y="257">Consult</tspan></text>
    <circle class="badge" cx="80" cy="292" r="54"/>
    <text class="badge-text" font-size="10"><tspan x="80" y="278">Custom Crafted</tspan><tspan x="80" y="290">Diet Plan</tspan><tspan x="80" y="302">To Achieve</tspan><tspan x="80" y="314">Your Goals</tspan></text>
    <circle class="badge" cx="287" cy="274" r="47"/>
    <text class="badge-text" font-size="9.5"><tspan x="287" y="256">Nutritionist</tspan><tspan x="287" y="268">Coaching</tspan><tspan x="287" y="280">To Improve</tspan><tspan x="287" y="292">Your Health</tspan><tspan x="287" y="304">And Vitality</tspan></text>
  </svg>

  <section class="product-info">
    <h1 class="product-title">Daily Harbor Plan</h1>
    <p class="product-price">$99.00</p>
    <p class="billing">No recurring billing</p>
    <p class="control">You're always in control of when you reorder.</p>
    <div class="buy">Buy it now</div>
    <p class="desc">This plan is designed for people who need to "lose a few pounds",<br>and who want expert consultation for overall health, and vitality.</p>
    <p class="includes">Plan includes:</p>
    <ul class="include-list">
      <li><strong>100% online</strong>. No need to visit the office.</li>
      <li>Expert nutrition consult</li>
      <li>Custom crafted diet plan to achieve your goals</li>
      <li>Nutrition coaching to improve your health and vitality</li>
      <li>Month-to-month pay as you go</li>
    </ul>
    <p class="exclusion"><strong>Does not</strong> include medication</p>
  </section>

</div>
</body>
</html>
```